Auto glass company

BRIGHTWAY
Roving Auto Glass, LLC
555-604-1937

* Windshield Replacement
* Rock Chip Repair
Danny "K"
Brightwayrovingautoglass@example.com
* Fully Insured

This is what I would like on the card. The image is what I had before. Looking for a logo possible too, couldn’t find a place to add that on. It’s a auto glass company.

Target Market(s)

Auto glass

Industry/Entity Type

Auto glass

Contact Information for Business Card

Logo, business name, phone number, windshield replacement, rock chip repair, insured, owner name Danny K, email address brightwayrovingautoglass@example.com

Colors

Designer to choose colors to be used in the design.

Requirements
Must have
• Logo, business name, phone number, windshield replacement, rock chip repair, insured, owner name Danny K, email address brightwayrovingautoglass@example.com

```html
<!DOCTYPE html>
<html lang="en">
<head>
<meta charset="utf-8">
<title>Brightway Roving Auto Glass – Business Card</title>
<link href="https://fonts.googleapis.com/css2?family=EB+Garamond:wght@400;600;700;800&family=Schoolbell&family=Open+Sans:wght@400&display=swap" rel="stylesheet">
<style>
  :root {
    --page-bg: #ffffff;
    --label-ink: #111111;
    --front-glass: #eef1f0;
    --front-glass-edge: #e3e8e6;
    --front-ink: #0d0d0d;
    --back-glass: #354043;
    --back-glass-edge: #2c3538;
    --back-ink: #ffffff;
  }
  * { box-sizing: border-box; margin: 0; padding: 0; }
  html, body {
    width: 802px; height: 1200px; overflow: hidden;
    background: var(--page-bg);
  }
  .sheet { position: relative; width: 802px; height: 1200px; }
  .side-label {
    position: absolute; left: 0; width: 802px; text-align: center;
    font-family: "Open Sans", sans-serif; font-size: 30px; color: var(--label-ink);
    line-height: 1;
  }
  .side-label--front { top: 45px; }
  .side-label--back { top: 582px; left: -6px; }

  .card {
    position: absolute; left: 53px; width: 698px; height: 452px; overflow: hidden;
  }
  .card--front { top: 90px; color: var(--front-ink); }
  .card--back { top: 628px; height: 454px; color: var(--back-ink); }

  .card__glass { position: absolute; inset: 0; }
  .card--front .card__glass {
    background: radial-gradient(circle at 58% 52%, var(--front-glass-edge) 0%, var(--front-glass) 55%);
  }
  .card--back .card__glass {
    background: radial-gradient(circle at 58% 50%, var(--back-glass-edge) 0%, var(--back-glass) 55%);
  }

  .centered {
    position: absolute; left: 0; width: 100%; text-align: center;
    transform: translateY(-50%); line-height: 1; white-space: nowrap;
  }
  .brand-name {
    top: 118px; left: 2px;
    font-family: "EB Garamond", serif; font-weight: 800; font-size: 68px; letter-spacing: 1px;
  }
  .brand-tagline {
    top: 182px; left: -14px;
    font-family: "EB Garamond", serif; font-weight: 400; font-size: 31px;
  }
  .phone {
    top: 278px; left: -8px;
    font-family: "Schoolbell", cursive; font-size: 74px; letter-spacing: 2px;
  }
  .phone-rule { position: absolute; left: 99px; top: 328px; width: 466px; height: 4px; }

  .services {
    position: absolute; top: 405px; left: 0; width: 100%;
    list-style: none; transform: translateY(-50%);
    font-family: "EB Garamond", serif; font-weight: 700; font-size: 18px; line-height: 1;
  }
  .services__item { position: absolute; top: 0; white-space: nowrap; transform: translateY(-50%); }
  .services__item::before {
    content: ""; display: inline-block; width: 13px; height: 13px; border-radius: 50%;
    background: var(--front-ink); margin-right: 7px; vertical-align: -1px;
  }
  .services__item--replacement { left: 18px; }
  .services__item--chip { left: 309px; }
  .services__item--insured { left: 531px; }

  .logo-slot {
    top: 148px; left: -6px;
    font-family: "EB Garamond", serif; font-weight: 400; font-size: 86px;
  }
  .owner {
    top: 297px; left: -8px;
    font-family: "EB Garamond", serif; font-weight: 400; font-size: 48px;
  }
  .email {
    top: 352px; left: -8px;
    font-family: "EB Garamond", serif; font-weight: 600; font-size: 19px;
  }
</style>
</head>
<body>
<main class="sheet">
  <p class="side-label side-label--front">Front</p>
  <section class="card card--front">
    <div class="card__glass" role="img" aria-label="Cracked windshield glass texture"></div>
    <h1 class="centered brand-name">BRIGHTWAY</h1>
    <p class="centered brand-tagline">Roving Auto Glass , LLC</p>
    <p class="centered phone">555-604-1937</p>
    <svg class="phone-rule" viewBox="0 0 466 4" preserveAspectRatio="none" aria-hidden="true">
      <line x1="0" y1="2" x2="466" y2="2" stroke="#222" stroke-width="1.5" stroke-dasharray="60 2 40 3 80 2"/>
    </svg>
    <ul class="services">
      <li class="services__item services__item--replacement">Windshield Replacement</li>
      <li class="services__item services__item--chip">RockChip Repair</li>
      <li class="services__item services__item--insured">Fully Insured</li>
    </ul>
  </section>

  <p class="side-label side-label--back">Back</p>
  <section class="card card--back">
    <div class="card__glass" role="img" aria-label="Dark cracked windshield glass texture"></div>
    <p class="centered logo-slot">Your Logo</p>
    <p class="centered owner">Danny “K”</p>
    <p class="centered email">brightwayrovingautoglass@example.com</p>
  </section>
</main>
</body>
</html>
```